**** Business card design for VoltaNode ****

For my ICT company VoltaNode I need I need a business card design.

We design, build and host web-applications and we have our own CMS product.

Some good examples are attached.

The information should be:
Joris Tielenburg
Managing director
E: j.tielenburg@voltanode-example.nl
M: +31(0)6 57218064
T: +31(0)40 7249305
W: www.voltanode-example.nl

Address:
Berend Vlootweg 27
5612 KT Eindhoven

Industry/Entity Type

Business

Requirements
Must have
• - Use logo (see attachments)
- Double sided
- Distinctive
Nice to have
• - Place for a statement on the back-side: "Designed with knowledge, built with passion"
- HTML code (or Wordpress)
- Dark (black or dark-gray) side
- Small simple images for telephone, e-mail en Url.
- QR code (only if not disturbing), not required, just an option

```html
<!DOCTYPE html>
<html lang="en">
<head>
<meta charset="utf-8">
<title>VoltaNode – Business Card</title>
<link rel="stylesheet" href="https://fonts.googleapis.com/css2?family=Audiowide&family=Black+Ops+One&display=swap">
<style>
  :root{
    --backdrop:#8c8c8c;
    --backdrop-light:#a8a8a8;
    --card-black:#000;
    --cyan:#27c6e0;
    --cyan-bright:#5fe8f5;
    --teal-text:#2d8ea8;
    --contact-blue:#2f7fb4;
    --icon-blue:#3a7fc0;
    --silver-light:#f4f4f4;
    --silver-mid:#9a9a9a;
    --silver-dark:#1c1c1c;
    --brand-slate:#3e5966;
    --tagline-blue:#1c9ccc;
  }
  *{margin:0;padding:0;box-sizing:border-box}
  html,body{width:900px;height:1200px;overflow:hidden}
  body{
    position:relative;
    background:linear-gradient(180deg,var(--backdrop-light),var(--backdrop));
    font-family:"Audiowide",sans-serif;
  }
  .card{position:absolute;left:15px;width:870px;overflow:hidden}
  .card--front{top:3px;height:580px;border-radius:45px;background:var(--card-black)}
  .card--back{
    top:597px;height:595px;border-radius:60px;
    background:radial-gradient(ellipse 70% 65% at 42% 42%,var(--silver-light) 0%,#d6d6d6 30%,var(--silver-mid) 62%,var(--silver-dark) 100%);
    box-shadow:inset 0 0 0 6px rgba(255,255,255,.25),inset 0 0 30px rgba(0,0,0,.6);
  }

  .streaks{position:absolute;opacity:.85}
  .streaks--top{left:0;top:0;width:870px;height:200px;
    background:linear-gradient(170deg,rgba(39,198,224,.55) 0%,rgba(39,198,224,.25) 45%,rgba(0,0,0,0) 100%);
    -webkit-mask-image:linear-gradient(180deg,#000 40%,transparent 100%);
    mask-image:linear-gradient(180deg,#000 40%,transparent 100%)}
  .streaks--bottom{left:300px;top:370px;width:570px;height:210px;
    background:linear-gradient(190deg,rgba(0,0,0,0) 0%,rgba(39,198,224,.3) 50%,rgba(39,198,224,.45) 100%);
    -webkit-mask-image:linear-gradient(90deg,transparent 0%,#000 45%);
    mask-image:linear-gradient(90deg,transparent 0%,#000 45%)}

  .swoosh{position:absolute;left:0;top:0;width:870px;height:580px}

  .title{
    position:absolute;left:0;width:946px;text-align:center;
    color:var(--teal-text);text-shadow:0 0 4px rgba(95,232,245,.4);
  }
  .title__role{top:225px;font-size:24px;letter-spacing:2px}
  .title__name{top:255px;font-size:38px;letter-spacing:3px}

  .contacts{position:absolute;left:14px;top:440px;list-style:none}
  .contacts__item{display:flex;align-items:center;height:34px;color:var(--contact-blue);font-size:18px}
  .contacts__icon{width:28px;height:28px;margin-right:10px;flex:none}

  .address{position:absolute;left:530px;top:484px;color:var(--contact-blue);font-size:18px;line-height:29px;font-style:normal}
  .address__label{letter-spacing:3px}

  .brand{position:absolute;left:210px;top:180px;display:flex;align-items:center}
  .brand__dot{width:100px;height:100px;border-radius:50%;background:var(--tagline-blue);margin-right:30px}
  .brand__name{font-size:78px;color:var(--brand-slate)}

  .tagline{
    position:absolute;left:0;width:870px;top:370px;text-align:center;
    font-family:"Black Ops One",sans-serif;font-size:34px;color:var(--tagline-blue);letter-spacing:1px;
  }
</style>
</head>
<body>

<section class="card card--front" aria-label="Business card front">
  <div class="streaks streaks--top" role="img" aria-label="Cyan digital light-streak pattern"></div>
  <div class="streaks streaks--bottom" role="img" aria-label="Cyan digital light-streak pattern"></div>

  <svg class="swoosh" viewBox="0 0 870 580" aria-hidden="true">
    <defs>
      <linearGradient id="swoosh-fill" x1="0" y1="0" x2="1" y2="0">
        <stop offset="0" stop-color="#27c6e0" stop-opacity=".9"/>
        <stop offset=".6" stop-color="#1a8fa8" stop-opacity=".55"/>
        <stop offset="1" stop-color="#0b3b48" stop-opacity=".2"/>
      </linearGradient>
    </defs>
    <path d="M0 440 C180 360 420 300 870 250 L870 290 C470 320 220 370 0 460 Z" fill="url(#swoosh-fill)"/>
    <path d="M0 440 C180 360 420 300 870 250" fill="none" stroke="#5fe8f5" stroke-width="3"/>
    <path d="M60 380 C260 300 520 250 870 200" fill="none" stroke="#27c6e0" stroke-width="1.5" opacity=".6"/>
  </svg>

  <p class="title title__role">Managing director</p>
  <h1 class="title title__name">Joris Tielenburg</h1>

  <ul class="contacts">
    <li class="contacts__item">
      <svg class="contacts__icon" viewBox="0 0 28 28" aria-hidden="true"><circle cx="14" cy="14" r="12.5" fill="none" stroke="#3a7fc0" stroke-width="2"/><rect x="7" y="9" width="14" height="10" fill="none" stroke="#3a7fc0" stroke-width="1.6"/><path d="M7 9 L14 15 L21 9" fill="none" stroke="#3a7fc0" stroke-width="1.6"/></svg>
      j.tielenburg@voltanode-example.nl
    </li>
    <li class="contacts__item">
      <svg class="contacts__icon" viewBox="0 0 28 28" aria-hidden="true"><circle cx="14" cy="14" r="12.5" fill="#3a7fc0"/><rect x="10" y="6" width="8" height="16" rx="1.5" fill="none" stroke="#fff" stroke-width="1.5"/><rect x="11.5" y="8.5" width="5" height="6" fill="#fff"/></svg>
      +31(0)6 57218064
    </li>
    <li class="contacts__item">
      <svg class="contacts__icon" viewBox="0 0 28 28" aria-hidden="true"><circle cx="14" cy="14" r="12.5" fill="none" stroke="#3a7fc0" stroke-width="2"/><path d="M9 8 C8 12 12 18 18 20 L20 17 L17 15 L15 16 C13 15 12 14 11 12 L12 10 L10 7 Z" fill="#3a7fc0"/></svg>
      +31(0)40 7249305
    </li>
    <li class="contacts__item">
      <svg class="contacts__icon" viewBox="0 0 28 28" aria-hidden="true"><circle cx="14" cy="14" r="12.5" fill="none" stroke="#3a7fc0" stroke-width="2"/><circle cx="14" cy="14" r="8" fill="none" stroke="#3a7fc0" stroke-width="1.4"/><ellipse cx="14" cy="14" rx="3.5" ry="8" fill="none" stroke="#3a7fc0" stroke-width="1.4"/><path d="M6 14 H22 M7.5 10 H20.5 M7.5 18 H20.5" stroke="#3a7fc0" stroke-width="1.2"/></svg>
      www.voltanode-example.nl
    </li>
  </ul>

  <address class="address">
    <span class="address__label">Address:</span><br>
    Berend Vlootweg 27<br>
    5612 KT Eindhoven
  </address>
</section>

<section class="card card--back" aria-label="Business card back">
  <div class="brand">
    <span class="brand__dot"></span>
    <span class="brand__name">VoltaNode</span>
  </div>
  <p class="tagline">Crafted with insight, shipped with care.</p>
</section>

</body>
</html>
```